Wholesale e-commerce website re-design

We are a wholesaler of African-made and African-themed products, and we're looking to update the look and feel of our website www.lomatrade.com to improve user experience. We'd like to have a cleaner homepage that keeps the product category menus (but simplifies them), allows certain products to be featured, and has a simple CTA box (something like "Login" for existing wholesale customers or "Start a Business" for new customers). The layout might be something along the lines of http://www.pinewellmarket.com/ except with a shopping cart featured at the top right. Our colors tend to be earth-toned, but the current color palate looks dated. Also see our blog.lomatrade.com page for themes and color ideas that are maybe more up-to-date. On our product pages, we want to feature the products more prominently and have simpler, cleaner Buy or Add buttons.

Other reference sites for inspiration: dravensupply.com, kettlorhome.com, http://www.pinewellmarket.com, http://morvanbulkgoods.com/ http://tenubra.com/
Updates

Project Deadline Extended
Reason: We like many of the designs that have been submitted so far, but need more time to make our final choice.

Target Market(s)

Small wholesale customers, most have a small business or home-based business. Also some retail, so an option for retail customers to click at the top to see retail pricing would be nice

Industry/Entity Type

Wholesale

Number of Pages Required

3 page

Font styles to use
Sans Serif

Requirements
Must have
• Clean, clear design that highlights products and reduces friction to customer purchase. Should include one homepage, one product page, and one shopping cart page design. Works with all browser types and be mobile-friendly.
Nice to have
• Other color schemes that would look good with our logo (maybe different from colors chosen below).
Should not have
• Splash pages with special effects, Adobe flash, elements that slow down page load times or that only work well in certain browsers.

```html
<!DOCTYPE html>
<html lang="en">
<head>
<meta charset="utf-8">
<title>Loma Trade – Wholesale African Goods</title>
<link rel="stylesheet" href="https://fonts.googleapis.com/css2?family=Montserrat:wght@600;800&family=Open+Sans:wght@400;600;700&family=Ubuntu:wght@400;500&display=swap">
<style>
:root{
  --pink:#f28a93;
  --yellow:#fdb813;
  --orange:#f7880f;
  --orange-dark:#d86a05;
  --price:#f27420;
  --ink:#2b2b2b;
  --muted:#666;
  --line:#d9d9d9;
  --white:#fff;
}
*{box-sizing:border-box;margin:0;padding:0}
html,body{width:879px;height:1200px;overflow:hidden;background:var(--white)}
body{position:relative;font-family:'Open Sans',sans-serif;color:var(--ink)}
.abs{position:absolute}
a{color:inherit;text-decoration:none}

/* top bar */
.topbar{left:0;top:0;width:879px;height:22px;background:var(--pink);color:var(--white);font-size:9px;display:flex;align-items:center;justify-content:space-between;padding:0 68px 0 70px}
.topbar span{display:inline-flex;align-items:center;gap:4px}
.topbar .links span+span::before{content:"|";margin:0 5px 0 3px;opacity:.9}
.topbar svg{width:9px;height:9px;fill:var(--white)}

/* header */
.brand{left:72px;top:58px;display:flex;align-items:center;gap:6px;font-family:'Ubuntu',sans-serif;font-weight:500;font-size:17px;color:#c8372f;letter-spacing:1px}
.brand .dot{width:12px;height:12px;border-radius:50%;background:#c8372f}
.search{left:335px;top:37px;width:326px;height:32px;border:1px solid #cfcfcf;display:flex}
.search span{flex:1;font-size:10px;color:#888;padding:9px 12px}
.search .btn{width:38px;border-left:1px solid #cfcfcf;display:flex;align-items:center;justify-content:center}
.cart{left:694px;top:38px;display:flex;gap:10px}
.cart .t1{font-size:11px;color:#555}
.cart .t2{font-size:8.5px;color:#888;margin-top:2px}
.nav{left:204px;font-size:10px;color:#555;display:flex}
.nav span{display:inline-flex;align-items:center}
.nav span::before{content:"";width:4px;height:4px;border-radius:50%;background:var(--yellow);margin-right:3px}
.rule{height:1px;background:var(--line)}

/* hero */
.hero{left:72px;top:162px;width:450px;height:287px;background:linear-gradient(100deg,#6a3d8f 0%,#c76d3a 30%,var(--orange) 55%,var(--orange) 100%)}
.hero-text{left:320px;top:205px;color:var(--white);font-family:'Montserrat',sans-serif}
.hero-text .kicker{font-size:16px;font-weight:600}
.hero-text h1{font-size:28px;font-weight:800;line-height:37px;margin-top:6px}
.btn-yellow{background:var(--yellow);color:var(--white);font-weight:700;border-radius:3px;display:flex;align-items:center;justify-content:center}
.hero .shop{left:252px;top:155px;width:114px;height:29px;font-size:11px}
.hero .arrows{left:386px;top:260px;display:flex;gap:2px}
.hero .arrows div{width:30px;height:27px;background:var(--orange-dark);display:flex;align-items:center;justify-content:center}

.cta{left:544px;top:162px;width:267px;height:287px;border:1px solid #444;text-align:center}
.cta h2{font-family:'Ubuntu',sans-serif;font-weight:500;font-size:20px;margin-top:88px;letter-spacing:.5px}
.cta h3{font-family:'Ubuntu',sans-serif;font-weight:400;font-size:18px;margin-top:2px}
.cta p{font-size:11.5px;color:#777;line-height:22px;margin-top:14px}
.cta .start{position:absolute;left:50px;top:215px;width:166px;height:35px;font-size:11px;box-shadow:0 2px 0 #e7a200}

/* featured */
.section-title{left:72px;top:498px;font-family:'Montserrat',sans-serif;font-size:18px;font-weight:800}
.section-title span{font-weight:600}
.pager{left:770px;top:502px;display:flex;gap:2px}
.pager div{width:20px;height:16px;background:#c8c8c8;display:flex;align-items:center;justify-content:center}
.card{top:550px;width:174px}
.card .pic{height:137px;border:1px solid #ccc;display:flex;align-items:center;justify-content:center}
.card .pic div{border-radius:4px}
.card h4{font-family:'Ubuntu',sans-serif;font-weight:400;font-size:13px;margin-top:14px}
.card .price{font-size:10.5px;margin-top:4px;color:#333}
.card .price b{color:var(--price);margin-right:3px}
.card p{font-size:8.8px;color:#555;line-height:15px;margin-top:7px;height:31px}
.card .actions{display:flex;justify-content:space-between;margin-top:6px}
.card .add{width:83px;height:24px;font-size:9px}
.card .view{width:83px;height:24px;font-size:9px;border:1px solid #bbb;border-radius:3px;color:var(--yellow);font-weight:700;display:flex;align-items:center;justify-content:center}

/* perks */
.perks{left:0;top:850px;width:879px;height:96px;background:var(--pink);color:var(--white)}
.perk{position:absolute;top:25px;display:flex;gap:10px}
.perk svg{fill:var(--white)}
.perk h5{font-family:'Ubuntu',sans-serif;font-weight:500;font-size:15px;margin-top:2px}
.perk small{display:block;font-size:9.5px;margin-top:2px;padding-left:2px}

/* footer */
.foot-brand{left:80px;top:1044px;flex-direction:column;align-items:flex-start;gap:6px;font-size:18px}
.vline{width:1px;background:#eee;top:970px;height:140px}
.fcol h6{font-family:'Ubuntu',sans-serif;font-weight:500;font-size:14px}
.fcol ul{list-style:none;margin-top:9px}
.fcol li{font-size:9px;color:#555;height:22px}
.fcol p{font-size:9px;color:#555;margin-top:10px}
.sub{left:570px;top:1034px;display:flex}
.sub .field{width:169px;height:26px;border:1px solid #ccc;font-size:9px;color:#555;padding:7px 9px}
.sub .go{width:68px;height:26px;font-size:9px;border-radius:0}
.social{left:567px;top:1098px;display:flex;gap:5px}
.social i{width:26px;height:26px;border-radius:50%;display:block}
.legal{left:72px;top:1167px;font-size:9px;color:#444}
.cards{left:634px;top:1163px;display:flex;gap:4px;align-items:center}
.cards i{display:block;width:24px;height:13px;border-radius:2px}
</style>
</head>
<body>

<div class="abs topbar">
  <div>
    <span><svg viewBox="0 0 10 10"><path d="M2 0l2 2-1 1.5a6 6 0 003.5 3.5L8 6l2 2-1.5 2C4 10 0 6 0 1.5z"/></svg>555 210 4477</span>
    <span style="margin-left:6px">| &nbsp;<svg viewBox="0 0 10 8"><path d="M0 0h10v8H0zM1 1l4 3 4-3"/></svg> info@lomatrade.com</span>
  </div>
  <div class="links">
    <span>Home</span><span>Item Quick Order</span><span>Web Specials</span><span>Top 10 Bestsellers</span><span>Your Account</span><span>Login</span>
  </div>
</div>

<div class="abs brand"><span class="dot"></span>LOMA TRADE</div>

<div class="abs search"><span>SEARCH</span><div class="btn"><svg width="14" height="14" viewBox="0 0 14 14" fill="none" stroke="#666" stroke-width="2"><circle cx="6" cy="6" r="4.5"/><path d="M9.5 9.5L13 13"/></svg></div></div>

<div class="abs cart">
  <svg width="26" height="24" viewBox="0 0 26 24" fill="none" stroke="#f6a623" stroke-width="2"><path d="M1 2h4l3 13h13l3-9H7"/><circle cx="10" cy="20" r="2"/><circle cx="19" cy="20" r="2"/></svg>
  <div><div class="t1">My Cart</div><div class="t2">0 Item(s) | $ 0.00 &nbsp;▾</div></div>
</div>

<div class="abs nav" style="top:87px;gap:0">
  <span style="width:107px">African Clothing</span><span style="width:101px">African Fabrics</span><span style="width:97px">African Soaps</span><span style="width:139px">Oils, Incense &amp; Burners</span><span style="width:108px">Health &amp; Beauty</span><span>New Items</span>
</div>
<div class="abs nav" style="top:112px">
  <span style="width:69px">Jewelry</span><span style="width:99px">Miscellaneous</span><span style="width:126px">Musical Instruments</span><span style="width:75px">Artwork</span><span style="width:129px">Clothing Accessories</span><span>All Categories</span>
</div>
<div class="abs rule" style="left:72px;top:138px;width:739px"></div>

<div class="abs hero" role="img" aria-label="Portrait of a woman in a purple head wrap and patterned top against an orange backdrop">
  <a class="abs btn-yellow shop">SHOP NOW &gt;&gt;</a>
  <div class="abs arrows">
    <div><svg width="8" height="12" viewBox="0 0 8 12" fill="none" stroke="#fff" stroke-width="2"><path d="M7 1L2 6l5 5"/></svg></div>
    <div><svg width="8" height="12" viewBox="0 0 8 12" fill="none" stroke="#fff" stroke-width="2"><path d="M1 1l5 5-5 5"/></svg></div>
  </div>
</div>
<div class="abs hero-text">
  <div class="kicker">NEW AFRICAN</div>
  <h1>CLOTHING &amp;<br>JEWELRY</h1>
</div>

<div class="abs cta">
  <svg style="position:absolute;left:113px;top:30px" width="42" height="38" viewBox="0 0 42 38" fill="var(--yellow)"><path d="M14 4h14v4h-3V6h-8v2h-3z"/><rect x="0" y="9" width="42" height="28" rx="4"/><rect x="7" y="9" width="3" height="28" fill="#fff"/><rect x="32" y="9" width="3" height="28" fill="#fff"/></svg>
  <h2>HOW TO START</h2>
  <h3>Your African Business</h3>
  <p>If you are a new customers , please Click<br>the link given below</p>
  <a class="btn-yellow start">START A BUSINESS</a>
</div>

<div class="abs rule" style="left:72px;top:475px;width:739px"></div>

<div class="abs section-title">FEATURED <span>PRODUCTS</span></div>
<div class="abs pager">
  <div><svg width="6" height="8" viewBox="0 0 6 8" fill="none" stroke="#fff" stroke-width="1.5"><path d="M5 1L2 4l3 3"/></svg></div>
  <div><svg width="6" height="8" viewBox="0 0 6 8" fill="none" stroke="#fff" stroke-width="1.5"><path d="M1 1l3 3-3 3"/></svg></div>
</div>

<div class="abs card" style="left:72px">
  <div class="pic"><div role="img" aria-label="Boxed bar of soap beside an unwrapped cream bar" style="width:94px;height:112px;background:linear-gradient(180deg,#5a4a22 0 48%,#e9e0c4 52% 100%)"></div></div>
  <h4>African Soaps</h4>
  <div class="price"><b>$1.49</b> per one</div>
  <p>Kessa Amber Soap is based on common rue extracts called Amber</p>
  <div class="actions"><a class="btn-yellow add">ADD TO CART</a><a class="view">VIEW DETAILS</a></div>
</div>
<div class="abs card" style="left:261px">
  <div class="pic"><div role="img" aria-label="Starter kit of bottles, soaps, packets and printed guides" style="width:150px;height:115px;background:linear-gradient(135deg,#3e3a36,#9fb28a 45%,#d9c9b8 80%,#eee)"></div></div>
  <h4>Easy Start Up Kit</h4>
  <div class="price"><b>$139.95</b> per one</div>
  <p>Perfect for anyone who wants to continue growing their business..</p>
  <div class="actions"><a class="btn-yellow add">ADD TO CART</a><a class="view">VIEW DETAILS</a></div>
</div>
<div class="abs card" style="left:450px">
  <div class="pic"><div role="img" aria-label="Bracelet of cowrie shells and colourful beads" style="width:112px;height:70px;border-radius:50%;background:radial-gradient(ellipse,#fff 0 35%,#e8dcc6 38%,#c9a96a 60%,#6a9a3a 75%,#fff 78%)"></div></div>
  <h4>Economical African Jewelry</h4>
  <div class="price"><b>$1.79</b> per one</div>
  <p>With jewelry, Africa is best known for its handmade bead work.</p>
  <div class="actions"><a class="btn-yellow add">ADD TO CART</a><a class="view">VIEW DETAILS</a></div>
</div>
<div class="abs card" style="left:638px">
  <div class="pic"><div role="img" aria-label="Wooden thumb piano" style="width:56px;height:92px;background:linear-gradient(160deg,#a57a44,#5a3a1c)"></div></div>
  <h4>Musical Instruments</h4>
  <div class="price"><b>$7.95</b> per one</div>
  <p>Loma Trade is the largest supplier of wholesale djembe drums</p>
  <div class="actions"><a class="btn-yellow add">ADD TO CART</a><a class="view">VIEW DETAILS</a></div>
</div>

<div class="abs perks">
  <div class="perk" style="left:72px">
    <svg width="40" height="46" viewBox="0 0 40 46"><rect x="2" y="2" width="36" height="36" rx="6"/><rect x="7" y="8" width="26" height="13" fill="var(--pink)"/><circle cx="10" cy="30" r="3" fill="var(--pink)"/><circle cx="30" cy="30" r="3" fill="var(--pink)"/><rect x="5" y="38" width="7" height="7" rx="2"/><rect x="28" y="38" width="7" height="7" rx="2"/></svg>
    <div><h5>Free Shipping</h5><small>Ducimus qui blanditiis</small></div>
  </div>
  <div class="perk" style="left:250px">
    <svg width="42" height="42" viewBox="0 0 42 42"><rect x="0" y="18" width="10" height="22" rx="2"/><path d="M13 18l9-16c4 0 6 3 5 7l-2 7h12c3 0 5 3 4 6l-4 14c-1 3-3 4-6 4H13z"/></svg>
    <div><h5>100% Guarantee</h5><small>Ducimus qui blanditiis</small></div>
  </div>
  <div class="perk" style="left:446px">
    <svg width="40" height="42" viewBox="0 0 40 42" fill="none" stroke="#fff" stroke-width="6"><path d="M6 20a14 14 0 0126-8"/><path d="M34 22a14 14 0 01-26 8"/><path d="M26 4l8 8-10 2z" fill="#fff" stroke-width="2"/><path d="M14 38l-8-8 10-2z" fill="#fff" stroke-width="2"/></svg>
    <div><h5>Free Returns</h5><small>Ducimus qui blanditiis</small></div>
  </div>
  <div class="perk" style="left:627px">
    <svg width="50" height="46" viewBox="0 0 50 46"><circle cx="25" cy="12" r="8"/><circle cx="10" cy="10" r="6"/><circle cx="40" cy="10" r="6"/><path d="M12 46V32a13 13 0 0126 0v14z"/><path d="M0 36v-8a9 9 0 0114-6v14z"/><path d="M50 36v-8a9 9 0 00-14-6v14z"/></svg>
    <div><h5>Customer Support</h5><small>Ducimus qui blanditiis</small></div>
  </div>
</div>

<div class="abs brand foot-brand"><span class="dot" style="width:14px;height:14px"></span>LOMA<br>TRADE</div>
<div class="abs vline" style="left:190px"></div>
<div class="abs vline" style="left:372px"></div>
<div class="abs vline" style="left:536px"></div>

<div class="abs fcol" style="left:222px;top:980px">
  <h6>Help &amp; support</h6>
  <ul><li>Recommended Reading</li><li>Submit your Story</li><li>Contact Us</li><li>Frequently Asked Questions</li><li>How to Order</li></ul>
</div>
<div class="abs fcol" style="left:404px;top:980px">
  <h6>My Account</h6>
  <ul><li>Delivery Information</li><li>My Account</li><li>Order Tracking</li><li>Reminder Service</li><li>Shipping, Returns &amp; Fees</li></ul>
</div>
<div class="abs fcol" style="left:570px;top:980px">
  <h6>Email Subscription</h6>
  <p>Register your email address to get information about us</p>
</div>
<div class="abs sub"><div class="field">Email Address</div><a class="btn-yellow go">SUBSCRIBE</a></div>
<div class="abs fcol" style="left:570px;top:1073px"><h6>Stay Connected</h6></div>
<div class="abs social">
  <i style="background:#4cb574"></i><i style="background:#3f63a8"></i><i style="background:#49b5e6"></i><i style="background:#d94a3a"></i><i style="background:#55739b"></i><i style="background:#4bc4e0"></i><i style="background:#c7201e"></i><i style="background:#d2232e"></i>
</div>

<div class="abs rule" style="left:72px;top:1142px;width:739px;background:#eee"></div>
<div class="abs legal">Copyrights © 2016, Loma Trade. All Rights Reserved &nbsp;| &nbsp; Privacy Policy | Terms of Use | Feedback</div>
<div class="abs cards">
  <i style="background:#2c7bbf"></i><i style="background:#1a3d8f"></i><i style="background:#e08a1e"></i><i style="background:#8a8a8a"></i><i style="background:#1f4f8f"></i><i style="background:#d33"></i>
</div>

</body>
</html>
```